この度はお世話になります。
出来ましたら過去にペットちゃんを飼ったことのある方、現在飼っている方にお願いしたいと思います。

また、表紙デザインですが、虹の橋を渡ったペットちゃんがお空の上でお花に囲まれ幸せそうな感じでお願いしたいです。

サブタイトルは絞り切れなかったので、良かったら本文を参考にお任せでお願い致します。
今回はプレゼントはないです。

ペットちゃん達が虹の橋を渡り、お花に囲まれ楽しそうにしている感じがよく表現されていると思いました。

この度はたくさんのご提案ありがとうございました。
次回は「ペットロス」についての書籍を考えていますので、ご縁がありましたら宜しくお願い致します。

```html
<!DOCTYPE html>
<html lang="ja">
<head>
<meta charset="UTF-8">
<title>後悔しないペット葬</title>
<link href="https://fonts.googleapis.com/css2?family=M+PLUS+Rounded+1c:wght@400;500;700&family=Noto+Sans+JP:wght@400;500&display=swap" rel="stylesheet">
<style>
  :root {
    --paper: #ffffff;
    --ink: #222222;
    --accent: #f39a2e;
    --band: #f5962a;
    --band-text: #ffffff;
    --skin-light: #f6dcc6;
    --skin-mid: #e9b896;
    --fur: #efe9e2;
  }
  * { margin: 0; padding: 0; box-sizing: border-box; }
  html, body { width: 750px; height: 1200px; overflow: hidden; background: var(--paper); }
  .cover {
    position: relative;
    width: 750px;
    height: 1200px;
    background: var(--paper);
    overflow: hidden;
  }
  .greeting {
    position: absolute;
    left: 96px;
    top: 28px;
    font-family: "M PLUS Rounded 1c", sans-serif;
    font-weight: 500;
    font-size: 98px;
    line-height: 1;
    color: var(--accent);
    letter-spacing: 4px;
  }
  .hands-photo {
    position: absolute;
    left: 40px;
    top: 160px;
    width: 710px;
    height: 185px;
  }
  .vertical {
    position: absolute;
    writing-mode: vertical-rl;
    font-family: "Noto Sans JP", sans-serif;
    color: var(--ink);
    line-height: 1;
    white-space: nowrap;
  }
  .subtitle {
    left: 440px;
    top: 342px;
    font-size: 74px;
    font-weight: 500;
    letter-spacing: -1px;
  }
  .title {
    left: 530px;
    top: 358px;
    font-size: 130px;
    font-weight: 500;
    letter-spacing: -6px;
  }
  .author-role {
    left: 102px;
    top: 612px;
    font-size: 24px;
    font-weight: 400;
    letter-spacing: 1px;
  }
  .author-name {
    left: 40px;
    top: 608px;
    font-size: 48px;
    font-weight: 500;
    letter-spacing: 1px;
  }
  .blurb-band {
    position: absolute;
    left: 0;
    top: 862px;
    width: 750px;
    height: 338px;
    background: var(--band);
    padding: 22px 0 0 22px;
  }
  .blurb-band p {
    font-family: "M PLUS Rounded 1c", sans-serif;
    font-weight: 400;
    font-size: 28px;
    line-height: 75px;
    color: var(--band-text);
    letter-spacing: 0.8px;
    white-space: nowrap;
  }
</style>
</head>
<body>
  <main class="cover">
    <div class="greeting">ありがとう</div>

    <svg class="hands-photo" role="img" aria-label="人の手のひらに犬の前足がそっと重ねられている写真" viewBox="0 0 710 185">
      <defs>
        <linearGradient id="handTone" x1="0" y1="0" x2="1" y2="0">
          <stop offset="0" stop-color="#efe9e2" stop-opacity="0.7"/>
          <stop offset="0.3" stop-color="#f6dcc6"/>
          <stop offset="0.75" stop-color="#e9b896"/>
          <stop offset="1" stop-color="#f6dcc6" stop-opacity="0.4"/>
        </linearGradient>
        <linearGradient id="fadeV" x1="0" y1="0" x2="0" y2="1">
          <stop offset="0" stop-color="#fff" stop-opacity="0"/>
          <stop offset="1" stop-color="#fff" stop-opacity="0.5"/>
        </linearGradient>
      </defs>
      <rect x="0" y="20" width="710" height="150" rx="75" fill="url(#handTone)"/>
      <rect x="0" y="20" width="710" height="150" rx="75" fill="url(#fadeV)"/>
    </svg>

    <div class="vertical subtitle">後悔しない</div>
    <h1 class="vertical title">ペット葬</h1>

    <div class="vertical author-role">陽だまり堂 代表</div>
    <div class="vertical author-name">森川さくら</div>

    <section class="blurb-band">
      <p>ペットの短い寿命、生きた証を残せないまま虹の</p>
      <p>橋を渡る。何も残せない命はあまりに悲しすぎる。</p>
      <p>ペットを家族に迎えた全ての飼い主様に今一度、</p>
      <p>ペットの大切さと命を考えて頂きたいと思います。</p>
    </section>
  </main>
</body>
</html>
```